Classy website for Corporate Entertainment - Action & Acrobatic Shows

12-Page Website to be coded using Wordpress!

We are "Velvet Summit Productions". We are all about providing 'experiences'! This website must be part of that experience :)

Please do not use our current website as inspiration for your design! We are looking for something new, and our business has outgrown that site (which was just for our shows) :)

We perform Action & Acrobatic Shows for corporate functions, as well as run Classes & Workshops from our Training Centre (Parkour, Acrobatics, etc), as well as Client Action Experiences and other services.

Example of our recent Morgan Vale 'Acrobatic Action Show' https://clipvault.example/watch/QxTr7nLpWzK

Our website must be super-classy/suave!! Needs to be heavily appealing to the Corporate community!

www.friendsphere.example/velvetsummitlive

Logo is available in the files below.
A series of photos have also been uploaded; please use any of these that you like throughout the design.

Menu Links from Home Page:
About Us (dropdown), Corporate Action Shows, Services (dropdown), Classes & Workshops (dropdown), The Ultimate Action Experience, Blog, Photos/Videos, Contact Us

PAGES:
- Home Page - must include a focus on Corporate Entertainment for the first glance, with information going down the page about our 4 major aspects: our Corporate Action Shows, Workshops & Classes, Services and Blog.

Required links on menu (menu does not necessarily have to be as a banner across the top - we are open to all ideas):

- Home Page

-"About Us" (dropdown with x2 pages "Our Shows" and "Our Team")

- Corporate Action Shows (x1 page)

- Services (dropdown with x3 pages "Action Showreels", and "Cosplay Competition Skits", and "Film & TV"

- Classes & Workshops (dropdown with x2 pages "Class Details & Prices" and "2016 Timetable"

- Ultimate Action Experience (x1 page with link to external website)

- Blog

- Videos & Photos or "See Us In Action" (x1 page)

- Contact Us

If you need more in-depth information into anything, please do not hesitate to send us a message!

Target Market(s)

Corporate (Classy)

Industry/Entity Type

Entertainment

Coding

Coded - Design and coding required

Number of Pages Required

5+ page

Requirements
Must have
• Website Coded via Wordpress

```html
<!DOCTYPE html>
<html lang="en">
<head>
<meta charset="utf-8">
<title>Velvet Summit Productions</title>
<link href="https://fonts.googleapis.com/css2?family=Roboto:wght@400;500;700;900&family=Libre+Baskerville&display=swap" rel="stylesheet">
<style>
:root{
  --red:#d0161c;
  --red-dark:#9e0f14;
  --black:#000;
  --panel:#0a0a0a;
  --card:#1c1c1c;
  --text:#fff;
  --muted:#8a8a8a;
  --dim:#4a4a4a;
  --line:#2a2a2a;
}
*{margin:0;padding:0;box-sizing:border-box}
html,body{width:672px;height:1200px;overflow:hidden}
body{position:relative;background:var(--black);font-family:'Roboto',Arial,sans-serif;color:var(--text)}
.abs{position:absolute}
.backdrop{position:absolute;left:0;top:88px;width:672px;height:1112px;
  background:radial-gradient(ellipse at 15% 20%,#7a1c34 0%,transparent 45%),radial-gradient(ellipse at 90% 40%,#6a1630 0%,transparent 45%),radial-gradient(ellipse at 10% 75%,#5e1428 0%,transparent 40%),radial-gradient(ellipse at 92% 85%,#6b1a33 0%,transparent 45%),linear-gradient(#3a0b18,#1b0710)}
.site-header{position:absolute;left:0;top:0;width:672px;height:88px;background:var(--black);border-bottom:3px solid var(--red)}
.brand{position:absolute;left:85px;top:11px;display:flex;align-items:center;gap:6px}
.brand-mark{width:26px;height:26px;border:2px solid #fff}
.brand-name{font-weight:900;font-size:12px;line-height:13px;text-transform:uppercase;color:#fff;width:70px}
.call{position:absolute;left:474px;top:12px;display:flex;align-items:center;gap:10px}
.call-icon{width:28px;height:28px;border-radius:50%;background:var(--red);display:flex;align-items:center;justify-content:center}
.call-label{font-size:10px;color:#ddd}
.call-number{font-size:13px;font-weight:500;color:#fff}
.header-rule{position:absolute;left:85px;top:55px;width:502px;border-top:1px dotted #333}
.main-nav{position:absolute;left:85px;top:66px;width:502px;display:flex;justify-content:space-between;padding:0 15px;font-size:6.5px;font-weight:500}
.panel{position:absolute;left:67px;top:106px;width:538px;height:1066px;background:var(--panel)}
.video{position:absolute;left:85px;top:120px;width:502px;height:243px;border:2px solid #777;
  background:radial-gradient(ellipse at 55% 45%,#5a3a2a 0%,#2a1a14 40%,#0c0908 80%)}
.video-bar{position:absolute;left:0;top:0;width:100%;height:26px;background:rgba(0,0,0,.45);display:flex;align-items:center;justify-content:space-between;padding:0 9px}
.video-title{font-size:11px;font-weight:700;text-transform:uppercase}
.video-tools{display:flex;gap:8px}
.play{position:absolute;left:229px;top:93px;width:40px;height:40px;border-radius:50%;border:2px solid #fff;background:rgba(0,0,0,.35);display:flex;align-items:center;justify-content:center;padding-left:3px}
.progress{position:absolute;left:0;top:220px;width:100%;height:4px;background:var(--red)}
.progress i{position:absolute;left:2px;top:-2px;width:8px;height:8px;border-radius:50%;background:#ddd}
.controls{position:absolute;left:0;top:224px;width:100%;height:17px;background:#111;display:flex;align-items:center;gap:12px;padding:0 12px;font-size:7px;color:#ccc}
.controls .grow{flex:1}
.section-title{position:absolute;font-size:12px;font-weight:700;text-transform:uppercase;padding-left:12px}
.section-title::before{content:"";position:absolute;left:0;top:-8px;width:26px;height:29px;border:1.5px solid #fff;border-right:none;border-bottom:none}
.section-title::after{content:"";position:absolute;left:0;bottom:-8px;width:1.5px;height:8px;background:#fff}
.section-title b{color:var(--red);font-weight:700}
.intro{position:absolute;left:140px;top:418px;width:392px;text-align:center;font-size:6.4px;line-height:12px;color:#ccc}
.card{position:absolute;top:459px;width:160px;height:225px;background:var(--card)}
.card-media{height:114px}
.card-body{padding:12px 10px}
.card-title{font-size:8.2px;font-weight:500;text-transform:uppercase}
.meta{font-size:4.8px;color:#bbb;margin-top:7px;display:flex;gap:8px}
.meta span::before{content:"";display:inline-block;width:4px;height:4px;border:1px solid var(--red);margin-right:3px}
.card-text{font-size:5.6px;line-height:11px;color:var(--muted);margin-top:6px}
.btn{display:inline-flex;align-items:center;gap:3px;background:var(--red);color:#fff;font-size:5.8px;font-weight:700;text-transform:uppercase;padding:5px 4px}
.btn::after{content:"";width:5px;height:5px;border:1px solid #fff;border-radius:50%}
.card .btn{margin-top:8px}
.divider{position:absolute;left:67px;top:702px;width:538px;border-top:1px solid #1e1e1e}
.post{position:absolute;left:85px;width:330px;height:92px}
.post-media{position:absolute;left:0;top:0;width:114px;height:92px;border:1px solid #555}
.post-actions{position:absolute;right:0;top:0;width:21px;height:70px;background:rgba(208,22,28,.75);display:flex;flex-direction:column;justify-content:space-around;align-items:center;font-size:5px}
.post-body{position:absolute;left:128px;top:3px;width:190px}
.post-title{font-size:7.2px;font-weight:500}
.post-text{font-size:5.4px;line-height:12px;color:var(--muted);margin:6px 0 10px}
.recent{position:absolute;left:414px;width:175px;display:flex;gap:10px}
.date{font-family:'Libre Baskerville',serif;color:var(--red);text-align:center;width:20px;border-right:1px dashed #444;padding-right:8px;box-sizing:content-box}
.date .d{font-size:14px;line-height:14px}
.date .m{font-size:9px;font-style:italic}
.recent-title{font-size:6.4px;font-weight:500}
.recent-text{font-size:5.5px;line-height:11px;color:var(--muted);margin-top:4px}
.footer-rule{position:absolute;left:67px;top:993px;width:538px;height:2px;background:var(--red)}
.foot-brand{top:1016px;left:85px}
.foot-about{position:absolute;left:85px;top:1058px;width:110px;font-size:5px;line-height:8px;color:var(--dim)}
.foot-about p+p{margin-top:6px}
.foot-head{position:absolute;top:1016px;font-size:7.5px;font-weight:500;text-transform:uppercase}
.foot-head::after{content:"";display:block;width:26px;height:2px;background:var(--red);margin-top:5px}
.mini-post{position:absolute;left:216px;display:flex;gap:7px;font-size:5px;color:var(--dim);width:115px}
.mini-date{width:21px;height:25px;border:1px solid #444;color:#ccc;text-align:center;font-size:5.5px;line-height:8px;padding-top:4px;flex:none}
.mini-post a{display:block;color:#ccc;margin-top:4px;text-decoration:none}
.news-text{position:absolute;left:348px;top:1046px;width:110px;font-size:5px;line-height:8px;color:var(--dim)}
.news-input{position:absolute;left:348px;top:1072px;width:111px;height:14px;background:#1b1b1b;font-size:5px;color:#ccc;padding:4px}
.news-btn{position:absolute;left:348px;top:1090px;width:45px;height:14px;background:var(--red);font-size:5px;font-weight:700;text-align:center;line-height:14px}
.gallery{position:absolute;left:483px;top:1045px;display:grid;grid-template-columns:repeat(3,32px);gap:2px}
.gallery div{height:29px;background:linear-gradient(#4a4a4a,#151515)}
.copy-rule{position:absolute;left:85px;top:1136px;width:502px;border-top:1px solid #1e1e1e}
.copyright{position:absolute;left:85px;top:1151px;font-size:5px;color:#bbb}
.social{position:absolute;left:499px;top:1144px;display:flex;gap:5px}
.social span{width:18px;height:18px;border:1px solid #777;border-radius:50%}
</style>
</head>
<body>
<div class="backdrop" role="img" aria-label="Blurred crowd at a red-lit corporate show"></div>

<header class="site-header">
  <div class="brand"><span class="brand-mark"></span><span class="brand-name">Velvet Summit</span></div>
  <div class="call">
    <span class="call-icon"><svg width="13" height="13" viewBox="0 0 24 24"><path fill="#fff" d="M6.6 10.8a15 15 0 006.6 6.6l2.2-2.2c.3-.3.7-.4 1-.2 1.1.4 2.3.6 3.6.6.6 0 1 .4 1 1V20c0 .6-.4 1-1 1A17 17 0 013 4c0-.6.4-1 1-1h3.5c.6 0 1 .4 1 1 0 1.3.2 2.5.6 3.6.1.3 0 .7-.2 1z"/></svg></span>
    <div><div class="call-label">Call us :</div><div class="call-number">(000)-555-0142</div></div>
  </div>
  <div class="header-rule"></div>
  <nav class="main-nav"><span>Home</span><span>About Us</span><span>Corporate Action Shows</span><span>Services</span><span>Classes &amp; Workshops</span><span>Action Experience</span><span>Blog</span><span>Photos/Videos</span><span>Contact Us</span></nav>
</header>

<main>
<div class="panel"></div>

<section class="video" role="img" aria-label="Video still of two performers in a staged fight">
  <div class="video-bar">
    <span class="video-title">Acrobatic Action Show</span>
    <span class="video-tools">
      <svg width="10" height="10" viewBox="0 0 10 10"><circle cx="8" cy="2" r="1.6" fill="#fff"/><circle cx="2" cy="5" r="1.6" fill="#fff"/><circle cx="8" cy="8" r="1.6" fill="#fff"/><path d="M8 2L2 5l6 3" stroke="#fff" fill="none"/></svg>
      <svg width="10" height="10" viewBox="0 0 10 10"><path d="M1 4h2v5H1zM4 9V4l2-3c1 0 1 1 1 2H9v2L8 9z" fill="none" stroke="#fff"/></svg>
      <svg width="10" height="10" viewBox="0 0 10 10"><circle cx="5" cy="5" r="4.5" fill="#fff"/><rect x="4.3" y="4" width="1.4" height="4" fill="#000"/><circle cx="5" cy="2.6" r=".8" fill="#000"/></svg>
    </span>
  </div>
  <div class="play"><svg width="14" height="14" viewBox="0 0 10 10"><path d="M2 1l7 4-7 4z" fill="#fff"/></svg></div>
  <div class="progress"><i></i></div>
  <div class="controls">
    <svg width="8" height="8" viewBox="0 0 10 10"><path d="M1 0l9 5-9 5z" fill="#aaa"/></svg>
    <svg width="9" height="8" viewBox="0 0 10 10"><path d="M0 3h3l3-3v10L3 7H0z" fill="#aaa"/></svg>
    <span>0:00 / 3:00</span><span class="grow"></span>
    <span>ClipVault</span>
    <svg width="8" height="8" viewBox="0 0 10 10"><path d="M0 3V0h3M7 0h3v3M10 7v3H7M3 10H0V7" stroke="#aaa" fill="none" stroke-width="1.5"/></svg>
  </div>
</section>

<h2 class="section-title" style="left:232px;top:390px">Welcome to <b>Velvet Summit</b></h2>
<p class="intro">It is a long established fact that a reader will be distracted by the readable content of a page when looking at its layout. The point of s that it has a more-or-less normal distribution of letters, as opposed readable English.</p>

<article class="card" style="left:84px">
  <div class="card-media" role="img" aria-label="Performers mid-stunt on a dark stage" style="background:linear-gradient(#3a2a2a,#6a3520 70%,#2a1510)"></div>
  <div class="card-body"><h3 class="card-title">Action Shows</h3>
    <div class="meta"><span>Oct 03, 2015</span><span>4 Comments</span><span>Written by Admin</span></div>
    <p class="card-text">It is a long established fact that a reader will be dis tracted by the readable content of a page when look read are Lorem Ipsum able English.</p>
    <span class="btn">Read More</span></div>
</article>
<article class="card" style="left:257px">
  <div class="card-media" role="img" aria-label="Silhouetted acrobat flipping at sunset" style="background:linear-gradient(#c9b29a,#8a6a55 60%,#2a2220)"></div>
  <div class="card-body"><h3 class="card-title">Classes at HQ</h3>
    <div class="meta"><span>Oct 03, 2015</span><span>4 Comments</span><span>Written by Admin</span></div>
    <p class="card-text">It is a long established fact that a reader will be dis tracted by the readable content of a page when look read are Lorem Ipsum able English.</p>
    <span class="btn">Read More</span></div>
</article>
<article class="card" style="left:429px">
  <div class="card-media" role="img" aria-label="Three performers posing with swords" style="background:linear-gradient(#e8e8e8,#b8b0aa 60%,#5a4a44)"></div>
  <div class="card-body"><h3 class="card-title">The Ultimate Action Experience</h3>
    <div class="meta"><span>Oct 03, 2015</span><span>4 Comments</span><span>Written by Admin</span></div>
    <p class="card-text">It is a long established fact that a reader will be dis tracted by the readable content of a page when look read are Lorem Ipsum able English.</p>
    <span class="btn">Read More</span></div>
</article>

<div class="divider"></div>

<h2 class="section-title" style="left:85px;top:723px">Latest <b>Blog</b></h2>
<h2 class="section-title" style="left:414px;top:723px">Recent <b>Posts</b></h2>

<article class="post" style="top:762px">
  <div class="post-media" role="img" aria-label="Red-lit gala dinner hall" style="background:linear-gradient(#c0204a,#6a1030 55%,#1a0810)">
    <div class="post-actions"><span>Like</span><span>Later</span><span>Share</span></div></div>
  <div class="post-body"><h3 class="post-title">Neque porro quisquam est qui dolorem</h3>
    <p class="post-text">It is a long established fact that a reader will be distracted by the readable content of a page when looking at its layout. The point of of letters making it look like readable EnglishIt is a long established of letters making it look like readable English</p>
    <span class="btn">Read More</span></div>
</article>
<article class="post" style="top:875px">
  <div class="post-media" role="img" aria-label="Silhouette of a jumping performer against a cloudy sky" style="background:linear-gradient(#dfe8ea,#8aa4aa 60%,#2a3a3e)">
    <div class="post-actions"><span>Like</span><span>Later</span><span>Share</span></div></div>
  <div class="post-body"><h3 class="post-title">Neque porro quisquam est qui dolorem</h3>
    <p class="post-text">It is a long established fact that a reader will be distracted by the readable content of a page when looking at its layout. The point of of letters making it look like readable EnglishIt is a long established of letters making it look like readable English</p>
    <span class="btn">Read More</span></div>
</article>

<div class="recent" style="top:766px"><div class="date"><div class="d">25</div><div class="m">gan</div></div><div><h4 class="recent-title">Velvet Summit - Acrobatic Action Shows</h4><p class="recent-text">It is a long established fact that a reader will be of letters making it look like readable English</p></div></div>
<div class="recent" style="top:821px"><div class="date"><div class="d">25</div><div class="m">gan</div></div><div><h4 class="recent-title">Velvet Summit - Acrobatic Action Shows</h4><p class="recent-text">It is a long established fact that a reader will be of letters making it look like readable English</p></div></div>
<div class="recent" style="top:876px"><div class="date"><div class="d">25</div><div class="m">gan</div></div><div><h4 class="recent-title">Velvet Summit - Acrobatic Action Shows</h4><p class="recent-text">It is a long established fact that a reader will be of letters making it look like readable English</p></div></div>
<div class="recent" style="top:926px"><div class="date"><div class="d">25</div><div class="m">gan</div></div><div><h4 class="recent-title">Velvet Summit - Acrobatic Action Shows</h4><p class="recent-text">It is a long established fact that a reader will be of letters making it look like readable English</p></div></div>
</main>

<footer>
  <div class="footer-rule"></div>
  <div class="brand abs foot-brand"><span class="brand-mark"></span><span class="brand-name">Velvet Summit</span></div>
  <div class="foot-about"><p>A stage for action, stunts and acrobatics built for corporate nights and events.</p><p>Book a show, a class or a full experience with our crew today.</p></div>

  <h4 class="foot-head" style="left:216px">Recents Posts</h4>
  <div class="mini-post" style="top:1046px"><div class="mini-date">25<br>FEB</div><div>Neque porro quisquam est qui dolorem ipsum quia<a href="#">Read more</a></div></div>
  <div class="mini-post" style="top:1087px"><div class="mini-date">25<br>FEB</div><div>Neque porro quisquam est qui dolorem ipsum quia<a href="#">Read more</a></div></div>

  <h4 class="foot-head" style="left:348px">Newsletters</h4>
  <p class="news-text">Neque porro quisquam est qui dolorem ipsum quia</p>
  <div class="news-input">Enter Your Email ID :</div>
  <div class="news-btn">SUBSCRIBE</div>

  <h4 class="foot-head" style="left:482px">Photo Gallery</h4>
  <div class="gallery" role="img" aria-label="Six small performance photos"><div></div><div></div><div></div><div></div><div></div><div></div></div>

  <div class="copy-rule"></div>
  <p class="copyright">© Copy Right2016. Velvet Summit. ALL RIGHTS RESERVED</p>
  <div class="social"><span></span><span></span><span></span><span></span></div>
</footer>
</body>
</html>
```